Business Card

Edit current business card design

Need business card design where Business Name, Logo, Address, phone and fax, website address are permanent.Need to be able to add and edit employee name and email address.

Industry/Entity Type

Business

```html
<!DOCTYPE html>
<html lang="en">
<head>
<meta charset="utf-8">
<title>Marlow's Accounting Service – Business Card</title>
<link href="https://fonts.googleapis.com/css2?family=Arimo:wght@400;700&display=swap" rel="stylesheet">
<style>
  :root {
    --page-bg: #e9e6e1;
    --card-white: #ffffff;
    --green-dark: #2f5e45;
    --green-mid: #3f7a57;
    --green-light: #5f9e74;
    --ink: #1c1c1c;
    --credential: #4b7a5c;
    --on-green: #ffffff;
  }
  * { box-sizing: border-box; margin: 0; padding: 0; }
  html, body {
    width: 1200px; height: 900px; overflow: hidden;
    background: var(--page-bg);
    font-family: "Arimo", Arial, sans-serif;
  }
  .sheet { position: relative; width: 1200px; height: 900px; }
  .card {
    position: absolute; left: 320px; width: 560px; height: 320px;
    background: var(--card-white);
    box-shadow: 0 6px 18px rgba(0,0,0,0.22);
    overflow: hidden;
  }
  .card--front { top: 110px; }
  .card--back { top: 470px; }

  /* front */
  .front-wave { position: absolute; inset: 0; }
  .business-name {
    position: absolute; left: 30px; top: 34px;
    font-size: 25px; font-weight: 700; color: var(--ink);
    text-shadow: 1px 1px 1px rgba(0,0,0,0.25);
  }
  .brand-mark {
    position: absolute; right: 26px; top: 22px;
    display: flex; align-items: center; gap: 8px;
  }
  .brand-mark__dot {
    width: 44px; height: 44px; border-radius: 50%;
    background: var(--green-mid);
  }
  .brand-mark__name { font-size: 17px; font-weight: 700; color: var(--green-dark); }
  .employee { position: absolute; left: 82px; top: 168px; }
  .employee__name { font-size: 23px; color: var(--ink); }
  .employee__credentials { font-size: 15px; color: var(--credential); margin-top: 4px; letter-spacing: 0.5px; }
  .contact {
    position: absolute; right: 20px; bottom: 20px;
    color: var(--on-green); font-size: 12px; line-height: 1.6;
    font-style: normal; text-align: right; white-space: nowrap;
  }
  .contact b { font-weight: 700; }

  /* back */
  .services-heading {
    position: absolute; right: 40px; top: 16px;
    font-size: 26px; font-weight: 700; color: var(--green-dark);
  }
  .services-band {
    position: absolute; left: 0; right: 0; top: 62px; height: 200px;
    background: radial-gradient(ellipse at 45% 50%, var(--green-light) 0%, var(--green-mid) 45%, var(--green-dark) 100%);
    padding: 16px 40px;
  }
  .services-list { list-style: none; color: var(--on-green); font-size: 14px; line-height: 28px; }
  .services-list li::before {
    content: ""; display: inline-block; width: 6px; height: 6px; border-radius: 50%;
    background: var(--on-green); margin-right: 12px; vertical-align: middle;
  }
  .tagline {
    position: absolute; left: 32px; bottom: 18px;
    font-size: 17px; color: var(--green-dark);
  }
</style>
</head>
<body>
<main class="sheet">
  <section class="card card--front">
    <svg class="front-wave" width="560" height="320" viewBox="0 0 560 320" aria-hidden="true">
      <defs>
        <radialGradient id="waveGreen" cx="0.62" cy="0.6" r="0.6">
          <stop offset="0" stop-color="#5f9e74"/>
          <stop offset="0.5" stop-color="#3f7a57"/>
          <stop offset="1" stop-color="#2f5e45"/>
        </radialGradient>
      </defs>
      <path d="M0 300 C 150 300, 210 250, 270 180 C 330 110, 400 80, 560 70 L560 320 L0 320 Z" fill="url(#waveGreen)"/>
      <path d="M0 286 C 150 286, 200 240, 258 170 C 318 98, 400 66, 560 58" fill="none" stroke="#3f7a57" stroke-width="6"/>
      <path d="M0 300 C 150 300, 210 250, 270 180 C 330 110, 400 80, 560 70" fill="none" stroke="#ffffff" stroke-width="5"/>
    </svg>
    <h1 class="business-name">Marlow's Accounting Service</h1>
    <div class="brand-mark">
      <span class="brand-mark__dot"></span>
      <span class="brand-mark__name">Marlow's</span>
    </div>
    <div class="employee">
      <p class="employee__name">Name Here</p>
      <p class="employee__credentials">EA,ATA,ATP</p>
    </div>
    <address class="contact">
      418 Birchwood Ave Ste 210 Lakeford, GA 30455<br>
      <b>Phone:</b> (555) 014-2231 | <b>Fax:</b> (555) 014-2298<br>
      <b>Email:</b> email@mailaddress.com | <b>Web:</b> www.marlowsacct.com
    </address>
  </section>

  <section class="card card--back">
    <h2 class="services-heading">Services</h2>
    <div class="services-band">
      <ul class="services-list">
        <li>Tax planning &amp; preparation for business &amp; individuals</li>
        <li>Tax problem resolutions</li>
        <li>Bookkeeping and Payroll Services</li>
        <li>Incorporation &amp; new business advisor</li>
        <li>Bookkeeping support &amp; training</li>
        <li>And more....</li>
      </ul>
    </div>
    <p class="tagline">Our Clients Keep More of What They Make</p>
  </section>
</main>
</body>
</html>
```